Pull Up Banners

Would like to have these pull up banner designs changed to a new modern theme. I have running a sales booth and want to re-design the banner designs. I have uploaded old banner design, I need phone number and website added onto bottom. Happy to consider images to attract people attention to increase sales and spark people interest walking past.

```html
<!DOCTYPE html>
<html lang="en">
<head>
<meta charset="utf-8">
<title>Deskline – Cloud Phone System &amp; Internet</title>
<link rel="stylesheet" href="https://fonts.googleapis.com/css2?family=Poppins:wght@400;700;800&family=Questrial&display=swap">
<style>
  :root {
    --brand-orange: #f26722;
    --ink: #0b0b0b;
    --header-black: #0a0a0a;
    --paper: #ffffff;
  }
  * { margin: 0; padding: 0; box-sizing: border-box; }
  html, body { width: 1200px; height: 3000px; overflow: hidden; background: var(--paper); }
  .banner { position: relative; width: 1200px; height: 3000px; background: var(--paper); overflow: hidden; }
  .banner-shapes { position: absolute; inset: 0; width: 1200px; height: 3000px; }

  .brand { position: absolute; top: 92px; left: 66px; display: flex; align-items: center; gap: 40px; }
  .brand-mark { width: 150px; height: 150px; border-radius: 50%; background: var(--brand-orange); }
  .brand-text { display: flex; flex-direction: column; }
  .brand-name {
    font-family: "Questrial", sans-serif; font-size: 112px; line-height: 1;
    letter-spacing: 8px; color: var(--brand-orange);
  }
  .brand-tagline {
    margin-top: 10px; font-family: "Poppins", sans-serif; font-size: 20px;
    letter-spacing: 5.2px; color: var(--paper);
  }

  .headline {
    position: absolute; top: 590px; left: 0; width: 1200px; text-align: center;
    font-family: "Poppins", sans-serif; font-weight: 800; font-size: 76px;
    line-height: 94px; color: var(--ink); letter-spacing: -0.5px;
  }

  .service { position: absolute; left: 233px; display: flex; align-items: center; }
  .service-icon {
    width: 224px; height: 224px; border-radius: 50%; background: var(--brand-orange);
    display: flex; align-items: center; justify-content: center; flex-shrink: 0;
  }
  .service-icon svg { width: 160px; height: 160px; }
  .service-label {
    margin-left: 74px; font-family: "Questrial", sans-serif; font-size: 64px;
    line-height: 76px; color: var(--ink); letter-spacing: 1px;
  }
  .service--voip { top: 897px; }
  .service--sms { top: 1257px; }
  .service--sms .service-label { margin-left: 86px; }
  .service--teams { top: 1619px; }
  .service--internet { top: 1979px; }

  .contact { position: absolute; left: 0; width: 1200px; text-align: center; color: var(--paper); font-family: "Poppins", sans-serif; font-weight: 700; }
  .contact-phone { top: 2608px; font-size: 86px; line-height: 100px; letter-spacing: 1px; }
  .contact-web { top: 2778px; font-size: 68px; line-height: 84px; }
</style>
</head>
<body>
<main class="banner">
  <svg class="banner-shapes" viewBox="0 0 1200 3000" aria-hidden="true">
    <rect x="0" y="0" width="1200" height="440" fill="var(--header-black)"/>
    <path d="M0 420 Q560 300 1200 412 L1200 440 L0 440 Z" fill="var(--brand-orange)"/>
    <path d="M0 426 Q560 332 1200 428 L1200 600 L0 600 Z" fill="var(--paper)"/>
    <path d="M0 2433 Q560 2560 1200 2413 L1200 3000 L0 3000 Z" fill="var(--brand-orange)"/>
  </svg>

  <header class="brand">
    <div class="brand-mark"></div>
    <div class="brand-text">
      <span class="brand-name">DESKLINE</span>
      <span class="brand-tagline">THE DESKLINE FOR ALL YOUR I.T SOLUTIONS</span>
    </div>
  </header>

  <h1 class="headline">CLOUD PHONE SYSTEM<br>&amp; INTERNET</h1>

  <section class="service service--voip">
    <div class="service-icon">
      <svg viewBox="0 0 100 100" fill="none" stroke="#fff" stroke-width="3" stroke-linecap="round" stroke-linejoin="round">
        <path d="M28 18 l10 -6 l12 20 l-8 6 q4 12 16 22 l8 -6 l16 16 l-8 8 q-24 2 -44 -26 q-10 -18 -2 -34 z"/>
        <path d="M60 26 q10 2 14 12"/>
        <path d="M62 16 q18 4 22 22"/>
      </svg>
    </div>
    <p class="service-label">VoIP &amp; Phone<br>Systems</p>
  </section>

  <section class="service service--sms">
    <div class="service-icon">
      <svg viewBox="0 0 100 100" fill="none" stroke="#fff" stroke-width="3" stroke-linejoin="round">
        <path d="M16 24 h68 a6 6 0 0 1 6 6 v32 a6 6 0 0 1 -6 6 h-54 l-10 10 v-10 h-4 a6 6 0 0 1 -6 -6 v-32 a6 6 0 0 1 6 -6 z"/>
        <circle cx="34" cy="46" r="5" fill="#fff" stroke="none"/>
        <circle cx="50" cy="46" r="5" fill="#fff" stroke="none"/>
        <circle cx="66" cy="46" r="5" fill="#fff" stroke="none"/>
      </svg>
    </div>
    <p class="service-label">SMS Gateway</p>
  </section>

  <section class="service service--teams">
    <div class="service-icon">
      <svg viewBox="0 0 100 100" fill="none" stroke="#fff" stroke-width="3" stroke-linejoin="round">
        <circle cx="26" cy="38" r="10"/>
        <circle cx="74" cy="38" r="10"/>
        <path d="M8 70 v-6 q0 -14 18 -14 q8 0 12 3 M92 70 v-6 q0 -14 -18 -14 q-8 0 -12 3 M8 70 h20 M72 70 h20"/>
        <circle cx="50" cy="36" r="12"/>
        <path d="M28 80 v-10 q0 -18 22 -18 q22 0 22 18 v10 z"/>
      </svg>
    </div>
    <p class="service-label">Unison Team<br>Calling</p>
  </section>

  <section class="service service--internet">
    <div class="service-icon">
      <svg viewBox="0 0 100 100" fill="none" stroke="#fff" stroke-width="3" stroke-linecap="round">
        <path d="M12 40 q38 -34 76 0"/>
        <path d="M24 52 q26 -22 52 0"/>
        <path d="M36 63 q14 -11 28 0"/>
        <circle cx="50" cy="78" r="6"/>
      </svg>
    </div>
    <p class="service-label">NBN, Fibre<br>&amp; 4G Internet</p>
  </section>

  <p class="contact contact-phone">1300 555 019</p>
  <p class="contact contact-web">Desklinecomputers.com.au</p>
</main>
</body>
</html>
```